Brindle Pizza gazebo signage project.

We are looking for signage for our mobile pizzeria gazebo structure. We sell pizza from a woodfired oven, Neapolitan style. We have a KT campervan which we sell pizza from too, which is yellow and black, so we would like to stick with those colours. The signage needs to be 2, 305cm x 76cm one for the top, and one for the bottom. It needs to state clearly the product is pizza. It also needs to include our logo, our website and that we sell Neapolitan style woodfired pizza. Our website is brindlepizza.co.uk to get a feel of our brand. We also don't want photos of pizza on the design.

Colors
000000
fbed22

Requirements
Must have
• The colours yellow and black and our logo on the top banner. Our website and the linkwave, peepsy and pixmoorly logos on the bottom banner.

```html
<!DOCTYPE html>
<html lang="en">
<head>
<meta charset="utf-8">
<title>Brindle Pizza – Gazebo Banners</title>
<link rel="stylesheet" href="https://fonts.googleapis.com/css2?family=Alfa+Slab+One&family=Arvo:wght@400;700&family=Permanent+Marker&display=swap">
<style>
  :root {
    --sun-yellow: #fbed22;
    --deep-yellow: #f7c600;
    --ink-black: #000000;
    --night-black: #070606;
    --line-grey: #3a3a3a;
    --signal-red: #e3001b;
  }
  html, body {
    margin: 0;
    padding: 0;
    width: 1200px;
    height: 1200px;
    overflow: hidden;
    background: #ffffff;
  }
  .canvas {
    position: relative;
    width: 1200px;
    height: 1200px;
  }
  .banner {
    position: absolute;
    left: 83px;
    width: 1046px;
    height: 261px;
    overflow: hidden;
  }
  .banner--top { top: 313px; background: var(--sun-yellow); }
  .banner--bottom { top: 617px; background: var(--night-black); }

  .banner__texture {
    position: absolute;
    inset: 0;
  }
  .banner--top .banner__texture {
    background: radial-gradient(ellipse at 25% 60%, rgba(247,198,0,0.35), transparent 55%),
                radial-gradient(ellipse at 75% 80%, rgba(247,198,0,0.3), transparent 50%);
  }
  .banner--bottom .banner__texture {
    background: radial-gradient(ellipse at 12% 50%, rgba(90,90,90,0.35), transparent 50%),
                radial-gradient(ellipse at 85% 40%, rgba(80,80,80,0.3), transparent 45%);
  }

  .brand-badge {
    position: absolute;
    left: 41px;
    top: 33px;
    width: 198px;
    height: 198px;
    border: 6px solid var(--ink-black);
    border-radius: 50%;
    box-sizing: border-box;
    display: flex;
    align-items: center;
    justify-content: center;
    text-align: center;
  }
  .brand-badge__name {
    font-family: "Alfa Slab One", serif;
    font-size: 34px;
    line-height: 1.05;
    color: var(--ink-black);
  }

  .headline {
    position: absolute;
    left: 270px;
    top: 42px;
    margin: 0;
    font-family: "Alfa Slab One", serif;
    font-weight: 400;
    font-size: 74px;
    line-height: 104px;
    color: var(--ink-black);
    white-space: nowrap;
  }

  .hand-note {
    position: absolute;
    font-family: "Permanent Marker", cursive;
    color: var(--signal-red);
    font-size: 20px;
    letter-spacing: 1px;
    text-transform: uppercase;
    white-space: nowrap;
  }
  .hand-note--social { left: 96px; top: 30px; }
  .hand-note--contact { left: 359px; top: 95px; }

  .social-list {
    position: absolute;
    left: 48px;
    top: 78px;
    margin: 0;
    padding: 0;
    list-style: none;
    display: flex;
    gap: 18px;
  }
  .social-list__item {
    font-family: "Arvo", serif;
    font-weight: 700;
    font-size: 18px;
    color: var(--sun-yellow);
  }

  .pointer-art {
    position: absolute;
    left: 400px;
    top: 45px;
    width: 100px;
    height: 42px;
    border-radius: 20px;
    background: linear-gradient(90deg, #c9b900, #8a7f10);
  }

  .contact-list {
    position: absolute;
    left: 533px;
    top: 34px;
    margin: 0;
    padding: 0;
    list-style: none;
    font-family: "Arvo", serif;
    font-size: 33px;
    line-height: 52px;
    color: var(--sun-yellow);
    white-space: nowrap;
  }
</style>
</head>
<body>
<main class="canvas">
  <section class="banner banner--top">
    <div class="banner__texture" role="img" aria-label="Faint line sketches of pizza and ingredients in deeper yellow"></div>
    <div class="brand-badge">
      <span class="brand-badge__name">Brindle<br>Pizza</span>
    </div>
    <h1 class="headline">Neapolitan Style<br>Woodfired Pizza</h1>
  </section>

  <section class="banner banner--bottom">
    <div class="banner__texture" role="img" aria-label="Faint grey line sketches of a pizza, peel and vegetables"></div>
    <span class="hand-note hand-note--social">Like us on</span>
    <ul class="social-list">
      <li class="social-list__item">peepsy</li>
      <li class="social-list__item">pixmoorly</li>
      <li class="social-list__item">linkwave</li>
    </ul>
    <div class="pointer-art" role="img" aria-label="Vintage pointing hand illustration"></div>
    <span class="hand-note hand-note--contact">Contact us</span>
    <ul class="contact-list">
      <li>07700 318452</li>
      <li>07700 629174</li>
      <li>info@brindlepizza.co.uk</li>
      <li>www.brindlepizza.co.uk</li>
    </ul>
  </section>
</main>
</body>
</html>
```